Innovative Event Ticketing Start Up. Needs a Web Design

We need a web design for a new company based in London called 'Bandwick'. We are a platform which facilitates the building of groups of customers for events. As more people commit to an event, the price incrementally decreases. We would like there to be an emphasis on the sharing element and the decreasing price with higher participation.

Any quieres please email me at rlvo57@mailtrove.net

Target Market(s)

18-30 year olds who are active and savvy across social media sites

Industry/Entity Type

Events

Number of Pages Required

3 page

Font styles to use
Other font styles liked:
• Phi Roman

Requirements
Must have
• Each event offering runs for a limited time so a countdown timer is also to be included as well as a counter of number of participants (please find example attached).
• The interface needs to have the options for 'Live 'Music', 'Nightlife', 'Festivals', 'Comedy' and 'Everything Else'. Also
• A 'featured' section, for our promoted events
• Social sharing icons for Chatterbarn, Quillow, PingMesh, SMS and Email
• Room the inclusion of a video
• Pages for clients to sign up - registering details ect.
• Content is still being completed, so room available to add when ready
Nice to have
• An interface design we like as a guiding templates on is https://kumvoxapp.com/
• Zamo wordpress theme is also of interest.
• Scroll over clicking for main interface and also for the event once clicked upon.
• Event pages similar desgin to kumvox with same features such as Trelvo Charts but also participant counter and affiliate marketing options.
Should not have
• CMS no longer necessary

```html
<!DOCTYPE html>
<html lang="en">
<head>
<meta charset="utf-8">
<title>Bandwick – Events</title>
<link href="https://fonts.googleapis.com/css2?family=Open+Sans:wght@400;600;700&display=swap" rel="stylesheet">
<style>
:root{
  --orange:#f15a24;
  --orange-light:#f7931e;
  --dark:#2b2b2b;
  --darker:#1f1f1f;
  --text:#555;
  --muted:#999;
  --line:#e5e5e5;
  --grey-bg:#f2f2f2;
  --white:#fff;
}
*{margin:0;padding:0;box-sizing:border-box}
html,body{width:1200px;height:2964px;overflow:hidden}
body{font-family:"Open Sans",Arial,sans-serif;color:var(--text);background:var(--white)}
.wrap{width:1000px;margin:0 auto;position:relative}

/* header */
.site-header{height:80px;display:flex;align-items:center;justify-content:space-between;padding:0 50px}
.brand{display:flex;align-items:center;gap:12px;font-weight:700;font-size:22px;color:var(--orange)}
.brand-box{width:44px;height:44px;background:var(--orange);border-radius:4px}
.nav{display:flex;gap:44px;font-size:13px;font-weight:600;text-transform:uppercase;color:#444;margin-left:auto;margin-right:40px}
.nav .active{color:var(--orange)}
.btn{display:inline-block;background:var(--orange);color:var(--white);font-weight:600;font-size:13px;text-transform:uppercase;padding:12px 22px;border-radius:3px}

/* hero */
.hero{height:568px;position:relative;background:radial-gradient(ellipse at 50% 20%,#f5d6c6 0%,#b98aa0 25%,#5a4a6e 55%,#241e2e 100%);text-align:center;color:var(--white)}
.hero-text{position:absolute;top:180px;left:0;right:0}
.hero h1{font-size:44px;font-weight:700;color:var(--orange);margin-bottom:24px}
.hero p{font-size:22px;font-weight:600;line-height:1.45;width:720px;margin:0 auto 34px}
.hero .btn{padding:16px 40px;background:var(--orange-light)}
.hero-arrow{position:absolute;top:260px;width:40px;height:40px;border-radius:50%;background:rgba(255,255,255,.35);display:flex;align-items:center;justify-content:center}
.hero-arrow.left{left:40px}.hero-arrow.right{right:40px}

/* section headings */
.section-title{text-align:center;font-size:26px;font-weight:700;color:#333;text-transform:uppercase}
.section-sub{text-align:center;font-size:11px;text-transform:uppercase;color:var(--muted);margin-top:10px;letter-spacing:.3px}

/* features */
.features{padding-top:60px;height:470px}
.feature-row{display:flex;justify-content:space-between;margin-top:50px}
.feature{width:220px;text-align:center}
.feature-icon{width:92px;height:92px;border:3px solid var(--orange);border-radius:50%;margin:0 auto 22px;display:flex;align-items:center;justify-content:center}
.feature h3{font-size:13px;font-weight:700;text-transform:uppercase;color:#333;margin-bottom:10px}
.feature p{font-size:12px;line-height:1.6;color:var(--muted)}
.divider{border-top:1px solid var(--line);margin-top:44px}

/* events */
.events-head{display:flex;justify-content:space-between;align-items:center}
.events-head h2{font-size:26px;font-weight:700;text-transform:uppercase;color:#333}
.events-head .sub{font-size:11px;text-transform:uppercase;color:var(--muted);margin-top:8px}
.pager{display:flex;gap:6px}
.pager span{width:26px;height:26px;background:#ccc;display:flex;align-items:center;justify-content:center;border-radius:2px}
.upcoming{padding-top:26px;height:516px}
.card-row{display:flex;justify-content:space-between;margin-top:28px}
.card{width:318px;background:#f7f7f7;box-shadow:0 1px 3px rgba(0,0,0,.15)}
.card-media{height:210px}
.card-body{padding:18px 18px 12px}
.card-body h4{font-size:14px;font-weight:700;color:var(--orange);text-transform:uppercase;margin-bottom:10px}
.card-body p{font-size:12px;line-height:1.6;color:var(--muted)}
.meta{display:flex;gap:16px;margin-top:12px;font-size:11px;color:var(--orange-light)}
.card-foot{height:36px;background:var(--dark);display:flex;justify-content:center;align-items:center;gap:8px}
.card-foot span{width:20px;height:20px;background:#555;border-radius:2px}

/* featured */
.featured{height:450px;background:linear-gradient(180deg,var(--orange) 0%,var(--orange-light) 100%);padding-top:50px;color:var(--white)}
.featured .events-head h2{color:var(--white)}
.featured .events-head .sub{color:rgba(255,255,255,.85)}
.featured .pager span{background:rgba(255,255,255,.5)}
.feat-row{display:flex;justify-content:space-between;margin-top:36px}
.feat-card{width:486px;display:flex;background:#fff;box-shadow:0 2px 6px rgba(0,0,0,.2)}
.feat-card .card-media{width:240px;height:240px}
.feat-info{flex:1;display:flex;flex-direction:column}
.feat-info .card-body{flex:1}

/* counters */
.counters{padding-top:64px;height:400px}
.counters .section-title{text-transform:none;font-size:24px}
.counter-row{display:flex;justify-content:space-between;margin-top:52px;padding:0 10px}
.counter{display:flex;align-items:center;gap:18px;width:300px}
.ring{position:relative;width:120px;height:120px;flex:none}
.ring b{position:absolute;inset:0;display:flex;flex-direction:column;align-items:center;justify-content:center;font-size:24px;color:var(--orange);font-weight:700}
.ring small{font-size:10px;color:var(--muted);font-weight:400}
.counter p{font-size:13px;font-weight:600;color:var(--orange);line-height:1.5}

/* bottom section */
.info{background:var(--grey-bg);height:396px;padding-top:44px}
.info-row{display:flex;justify-content:space-between;align-items:flex-start}
.info h5{font-size:14px;font-weight:700;color:#333;margin-bottom:18px}
.map,.video{width:340px;height:240px}
.map{background:linear-gradient(135deg,#e9e4d8,#d7dfcf)}
.video{background:linear-gradient(180deg,#c9d6e4,#7a6a6a);position:relative}
.play{position:absolute;left:50%;top:50%;width:52px;height:36px;margin:-18px 0 0 -26px;background:var(--orange);border-radius:8px;display:flex;align-items:center;justify-content:center}
.form{width:260px;background:#fff;margin-top:-20px;box-shadow:0 1px 3px rgba(0,0,0,.15)}
.form-head{background:var(--orange);color:#fff;font-weight:700;font-size:14px;padding:12px;text-align:center}
.form-body{padding:14px 16px 16px}
.form-body label{display:block;font-size:10px;color:var(--muted);margin-bottom:4px}
.form-body .field{height:24px;border:1px solid var(--line);margin-bottom:10px}
.form-body .btn{display:block;text-align:center;padding:8px;font-size:11px;background:var(--orange-light)}

.site-footer{height:84px;background:var(--darker);display:flex;align-items:center;justify-content:space-between;padding:0 100px;font-size:11px;color:#999}
.connect{display:flex;align-items:center;gap:8px}
.connect i{width:28px;height:28px;border-radius:50%;background:var(--orange);display:inline-block}
.connect i:nth-child(2){background:#3b8fd1}
.connect i:nth-child(3){background:#3a5a99}
</style>
</head>
<body>

<header class="site-header">
  <div class="brand"><span class="brand-box"></span>Bandwick</div>
  <nav class="nav">
    <span class="active">Home</span><span>About</span><span>Features</span><span>Events</span><span>Blog</span><span>Contact</span>
  </nav>
  <span class="btn">Register or Log in</span>
</header>

<section class="hero" role="img" aria-label="Concert crowd with raised hands under bright stage lights">
  <span class="hero-arrow left"><svg width="14" height="14" viewBox="0 0 14 14"><path d="M9 2 4 7l5 5" stroke="#fff" stroke-width="2" fill="none"/></svg></span>
  <span class="hero-arrow right"><svg width="14" height="14" viewBox="0 0 14 14"><path d="m5 2 5 5-5 5" stroke="#fff" stroke-width="2" fill="none"/></svg></span>
  <div class="hero-text">
    <h1>Soluta nobis est eligendi</h1>
    <p>Nam libero tempore, cum soluta nobis est eligendi optio cumque nihil impedit quo minus id quod maxime placeat...</p>
    <span class="btn">Click Here More</span>
  </div>
</section>

<section class="features wrap">
  <h2 class="section-title">Features</h2>
  <p class="section-sub">Simply dummy text of the printing and typesetting industry. Lorem ipsum has been the industry's standard dummy text</p>
  <div class="feature-row">
    <div class="feature">
      <div class="feature-icon"><svg width="36" height="32" viewBox="0 0 36 32"><path d="M18 30 4 16A8 8 0 0 1 18 6a8 8 0 0 1 14 10Z" fill="var(--orange)"/></svg></div>
      <h3>News Emini Ipsum</h3><p>Lorem ipsum dolor sit amet consectetur adipiscing elit sed do eiusmod tempor incididunt ut labore.</p>
    </div>
    <div class="feature">
      <div class="feature-icon"><svg width="40" height="32" viewBox="0 0 40 32"><circle cx="20" cy="9" r="6" fill="var(--orange)"/><circle cx="8" cy="12" r="4" fill="var(--orange)"/><circle cx="32" cy="12" r="4" fill="var(--orange)"/><path d="M10 30a10 10 0 0 1 20 0Z M1 30a7 7 0 0 1 12-5v5Z M39 30a7 7 0 0 0-12-5v5Z" fill="var(--orange)"/></svg></div>
      <h3>News Emini Ipsum</h3><p>Lorem ipsum dolor sit amet consectetur adipiscing elit sed do eiusmod tempor incididunt ut labore.</p>
    </div>
    <div class="feature">
      <div class="feature-icon"><svg width="36" height="30" viewBox="0 0 36 30"><path d="M22 2 34 12 22 22v-6C12 16 6 20 2 28 3 16 10 8 22 8Z" fill="var(--orange)"/></svg></div>
      <h3>News Emini Ipsum</h3><p>Lorem ipsum dolor sit amet consectetur adipiscing elit sed do eiusmod tempor incididunt ut labore.</p>
    </div>
    <div class="feature">
      <div class="feature-icon"><svg width="36" height="36" viewBox="0 0 36 36"><circle cx="18" cy="18" r="14" stroke="var(--orange)" stroke-width="3" fill="none"/><path d="M18 9v10l6 4" stroke="var(--orange)" stroke-width="3" fill="none"/></svg></div>
      <h3>News Emini Ipsum</h3><p>Lorem ipsum dolor sit amet consectetur adipiscing elit sed do eiusmod tempor incididunt ut labore.</p>
    </div>
  </div>
  <div class="divider"></div>
</section>

<section class="upcoming wrap">
  <div class="events-head">
    <div><h2>Upcoming Events</h2><p class="sub">Simply dummy text of the printing and typesetting industry. Lorem ipsum has been the industry's standard dummy text</p></div>
    <div class="pager"><span></span><span></span></div>
  </div>
  <div class="card-row">
    <article class="card">
      <div class="card-media" role="img" aria-label="Studio microphone in blue light" style="background:linear-gradient(135deg,#0e3a5c,#2aa3c9)"></div>
      <div class="card-body"><h4>Live Music</h4><p>Lorem ipsum dolor sit amet consectetur adipiscing elit sed do eiusmod tempor incididunt ut labore dolore.</p>
        <div class="meta"><span>12 Aug 2015 6:30 PM</span><span>London, UK</span></div></div>
      <div class="card-foot"><span></span><span></span><span></span></div>
    </article>
    <article class="card">
      <div class="card-media" role="img" aria-label="Nightclub crowd under warm stage lights" style="background:linear-gradient(180deg,#e9a63a,#5a2a10)"></div>
      <div class="card-body"><h4>Nightlife</h4><p>Lorem ipsum dolor sit amet consectetur adipiscing elit sed do eiusmod tempor incididunt ut labore dolore.</p>
        <div class="meta"><span>14 Aug 2015 9:00 PM</span><span>London, UK</span></div></div>
      <div class="card-foot"><span></span><span></span><span></span></div>
    </article>
    <article class="card">
      <div class="card-media" role="img" aria-label="Friends dancing at a festival party" style="background:linear-gradient(135deg,#6a2a7a,#d14a8a)"></div>
      <div class="card-body"><h4>Festivals</h4><p>Lorem ipsum dolor sit amet consectetur adipiscing elit sed do eiusmod tempor incididunt ut labore dolore.</p>
        <div class="meta"><span>20 Aug 2015 2:00 PM</span><span>London, UK</span></div></div>
      <div class="card-foot"><span></span><span></span><span></span></div>
    </article>
  </div>
</section>

<section class="featured">
  <div class="wrap">
    <div class="events-head">
      <div><h2>Featured Events</h2><p class="sub">Simply dummy text of the printing and typesetting industry. Lorem ipsum has been the industry's standard dummy text</p></div>
      <div class="pager"><span></span><span></span></div>
    </div>
    <div class="feat-row">
      <article class="feat-card">
        <div class="card-media" role="img" aria-label="Comedy theatre masks on a red backdrop" style="background:linear-gradient(135deg,#b3202a,#f2b632)"></div>
        <div class="feat-info">
          <div class="card-body"><h4>Comedy</h4><p>Lorem ipsum dolor sit amet consectetur adipiscing elit sed do eiusmod tempor incididunt ut labore et dolore magna.</p>
            <div class="meta"><span>22 Aug 2015</span><span>London, UK</span></div></div>
          <div class="card-foot"><span></span><span></span><span></span></div>
        </div>
      </article>
      <article class="feat-card">
        <div class="card-media" role="img" aria-label="Open air festival stage under blue sky" style="background:linear-gradient(180deg,#6fb6e6,#c9a070)"></div>
        <div class="feat-info">
          <div class="card-body"><h4>Festivals</h4><p>Lorem ipsum dolor sit amet consectetur adipiscing elit sed do eiusmod tempor incididunt ut labore et dolore magna.</p>
            <div class="meta"><span>28 Aug 2015</span><span>London, UK</span></div></div>
          <div class="card-foot"><span></span><span></span><span></span></div>
        </div>
      </article>
    </div>
  </div>
</section>

<section class="counters wrap">
  <h2 class="section-title">Participant Counter</h2>
  <div class="counter-row">
    <div class="counter">
      <div class="ring"><svg width="120" height="120" viewBox="0 0 120 120"><circle cx="60" cy="60" r="52" stroke="#eee" stroke-width="8" fill="none"/><circle cx="60" cy="60" r="52" stroke="var(--orange-light)" stroke-width="8" fill="none" stroke-dasharray="245 327" transform="rotate(-90 60 60)"/></svg><b>570<small>People</small></b></div>
      <p>Nemo enim ipsam voluptatem quia voluptas sit aspernatur...</p>
    </div>
    <div class="counter">
      <div class="ring"><svg width="120" height="120" viewBox="0 0 120 120"><circle cx="60" cy="60" r="52" stroke="#eee" stroke-width="8" fill="none"/><circle cx="60" cy="60" r="52" stroke="var(--orange-light)" stroke-width="8" fill="none" stroke-dasharray="280 327" transform="rotate(-90 60 60)"/></svg><b>678<small>People</small></b></div>
      <p>Nemo enim ipsam voluptatem quia voluptas sit aspernatur...</p>
    </div>
    <div class="counter">
      <div class="ring"><svg width="120" height="120" viewBox="0 0 120 120"><circle cx="60" cy="60" r="52" stroke="#eee" stroke-width="8" fill="none"/><circle cx="60" cy="60" r="52" stroke="var(--orange-light)" stroke-width="8" fill="none" stroke-dasharray="190 327" transform="rotate(-90 60 60)"/></svg><b>345<small>People</small></b></div>
      <p>Nemo enim ipsam voluptatem quia voluptas sit aspernatur...</p>
    </div>
  </div>
</section>

<section class="info">
  <div class="wrap info-row">
    <div><h5>Our Locations</h5><div class="map" role="img" aria-label="Street map with a location pin"></div></div>
    <div><h5>Our Video</h5><div class="video" role="img" aria-label="Festival crowd video still"><span class="play"><svg width="16" height="16" viewBox="0 0 16 16"><path d="M4 2 14 8 4 14Z" fill="#fff"/></svg></span></div></div>
    <div class="form">
      <div class="form-head">Registration Form</div>
      <div class="form-body">
        <label>Full Name</label><div class="field"></div>
        <label>Email Address</label><div class="field"></div>
        <label>Password</label><div class="field"></div>
        <span class="btn">Register Now</span>
      </div>
    </div>
  </div>
</section>

<footer class="site-footer">
  <span>Copyright © Bandwick 2015 | All rights reserved</span>
  <div class="connect"><span>Connect with us</span><i></i><i></i><i></i><i></i></div>
</footer>

</body>
</html>
```